Website Design for a Graphic Design Studio in California

We are working with a graphic design company in California.
PLEASE NOTE: We report and ban any designer that reaches out directly to our customers.

Some sites to use for content/competitors and inspiration:

http://quelvint.co.uk
https://www.fendro.studio
https://www.zuplo.io (Client's Favorite)
https://www.merigoldcrafts.com
https://craftwimble.com
https://www.dravinsultonmask.com/us/home/

Thank you for taking the time to consider designing a website for us. We are web developers based in Stockton, CA, USA. Most of our projects go through the same process. Understanding this process may help you win a project with us. We custom-code all of our websites in-house. We don’t have any requirements as to what tools you use for your design, but we prefer Figma files. For any design that we label as four-stars, we send it to the client for review. The client picks the final design they want us to use. Once we complete this process, we will continue to show additional clients all the four-star sites and purchase them later. Your designs will have multiple chances to sell. For better chances of success, we ask that you follow these guidelines.

IMAGES:
If you use any images or icons in the design, we ask that you have a link to the asset so we can purchase the image/icon. Most of the designs we submit do not have the customer’s images on them unless they have some great images. Be creative; show us the feeling you are trying to portray with your image choices. Use any royalty-free site you choose. We subscribe to Tessaly and mainly use their images, but we can purchase images outside of Tessaly. PLEASE NOTE: we will not submit designs to clients with watermarks on the images.

FONTS:
We ask that you identify the fonts used in the design. This can be done in a message if you want. We typically use Brindle Fonts and Tessaly Fonts.

CONTENT:
We're always open to different content and ideas. We often submit designs with stock images so the client can see our vision. We typically take pictures after the website launch to use their images with our vision. Lorem Ipsum is fine for paragraphs, but we ask that you write the headers in correct English. We want to be able to show the vision and identify the sections of the website.

INSPIRATION:
We typically add a couple of links in the brief of websites we like to help you get started in your design.

REVISIONS:
We do not often ask for revisions of the designs unless we see something in the design that may not appeal to the client. If there are slight changes that we want to make, we do that in the development process.

FEEDBACK:
We rarely give feedback on designs during the design process. We are working on many website projects and do not have the time to provide feedback. We usually respond if your request is well thought out and asks specific questions, but a note asking “feedback, please” usually goes unanswered.

```html
<!DOCTYPE html>
<html lang="en">
<head>
<meta charset="utf-8">
<title>Verantum — Branding and Package Design</title>
<link rel="stylesheet" href="https://fonts.googleapis.com/css2?family=Cinzel:wght@400&family=Questrial&family=Arimo:wght@400&family=Tenor+Sans&family=Urbanist:wght@600&display=swap">
<style>
  :root {
    --ink: #000000;
    --paper: #ffffff;
    --gold: #d9a84e;
  }
  html, body {
    margin: 0;
    padding: 0;
    width: 1200px;
    height: 704px;
    overflow: hidden;
    background: var(--ink);
  }
  .page {
    position: relative;
    width: 1200px;
    height: 704px;
    background: var(--ink);
    color: var(--paper);
  }
  .brand {
    position: absolute;
    left: 83px;
    top: 78px;
    display: flex;
    align-items: center;
    gap: 12px;
    font-family: "Questrial", sans-serif;
    font-size: 26px;
    color: var(--paper);
    text-decoration: none;
  }
  .brand-dot {
    width: 30px;
    height: 30px;
    border-radius: 50%;
    background: var(--gold);
  }
  .main-nav {
    position: absolute;
    top: 84px;
    right: 83px;
    display: flex;
    gap: 56px;
  }
  .main-nav a {
    font-family: "Questrial", sans-serif;
    font-size: 20px;
    color: var(--paper);
    text-decoration: none;
    line-height: 1;
  }
  .hero-title {
    position: absolute;
    left: 314px;
    top: 218px;
    width: 806px;
    margin: 0;
    font-family: "Cinzel", serif;
    font-weight: 400;
    font-size: 117px;
    line-height: 1;
    letter-spacing: 0.01em;
    color: var(--gold);
    white-space: nowrap;
  }
  .tagline {
    position: absolute;
    left: 317px;
    top: 357px;
    margin: 0;
    font-family: "Arimo", sans-serif;
    font-size: 28px;
    letter-spacing: 0.12em;
    color: var(--paper);
    white-space: nowrap;
  }
  .intro {
    position: absolute;
    left: 82px;
    top: 463px;
    width: 420px;
    margin: 0;
    font-family: "Tenor Sans", sans-serif;
    font-size: 28px;
    line-height: 36.7px;
    letter-spacing: 0.01em;
    color: var(--paper);
  }
  .cta {
    position: absolute;
    left: 869px;
    top: 579px;
    width: 248px;
    height: 47px;
    display: flex;
    align-items: center;
    justify-content: center;
    background: var(--gold);
    color: var(--paper);
    font-family: "Urbanist", sans-serif;
    font-weight: 600;
    font-size: 21px;
    text-decoration: none;
  }
</style>
</head>
<body>
  <div class="page">
    <header>
      <a class="brand" href="#"><span class="brand-dot"></span>Verantum</a>
      <nav class="main-nav">
        <a href="#">About</a>
        <a href="#">Services</a>
        <a href="#">Products</a>
        <a href="#">Contact</a>
      </nav>
    </header>
    <main>
      <h1 class="hero-title">VERANTUM</h1>
      <p class="tagline">Designing your tomorrow, today.</p>
      <p class="intro">As a full–service branding and package design agency. We are experts at increasing the value of your brand with imagination, ingenuity and passion.</p>
      <a class="cta" href="#">Schedule a Call</a>
    </main>
  </div>
</body>
</html>
```